Harlow Ridge Growers and Nursery needs a business street sign.

I have three businesses located at the same address: The Harlow Ridge Growers & Nursery, The Bramble Nook, and The Quarry Commons. I am looking for a 4’ x 8’ street sign to represent all three businesses as one retail experience. It needs to be eye catching yet simple enough that people can fully read it while driving by. I have logos for the greenhouse and village however I do not have anything for The Bramble Nook. I’m looking for some type of font that’s similar or in between the two attached logos for The Bramble Nook.

• Horizontal Sign, Eye catching, yet simple design so people see it while driving by.
• Horizontal Sign
• I’m open to the design being both vertical and horizontal. Please provide both options

```html
<!DOCTYPE html>
<html lang="en">
<head>
<meta charset="utf-8">
<title>Harlow Ridge Growers &amp; Nursery — Street Sign</title>
<link rel="stylesheet" href="https://fonts.googleapis.com/css2?family=Playfair+Display:wght@800&display=swap">
<style>
  :root {
    --backdrop: #3b3b3b;
    --sign-cream: #e4e0d4;
    --nursery-green: #1f6b3f;
    --commons-brown: #92302a;
    --nook-red: #e8384f;
    --flourish-tint: #e9c9c8;
    --divider-grey: #6e6e6e;
    --meadow-light: #7fd04a;
    --meadow-deep: #2f9a24;
  }
  * { margin: 0; padding: 0; box-sizing: border-box; }
  html, body {
    width: 1200px; height: 1200px; overflow: hidden;
    background: var(--backdrop);
  }
  .street-sign {
    position: absolute; left: 54px; top: 327px;
    width: 1092px; height: 546px;
    background: var(--sign-cream);
    overflow: hidden;
    font-family: "Playfair Display", Georgia, serif;
    font-weight: 800;
  }
  .partner-name {
    position: absolute;
    text-align: center;
    white-space: nowrap;
  }
  .partner-name--nursery {
    left: 70px; top: 86px; width: 447px;
    color: var(--nursery-green);
    font-size: 44px; line-height: 1.15;
  }
  .partner-name--commons {
    left: 601px; top: 68px; width: 426px;
    color: var(--commons-brown);
    font-size: 62px; line-height: 1.1;
  }
  .brand-divider {
    position: absolute; left: 562px; top: 34px;
    width: 3px; height: 192px;
    background: var(--divider-grey);
  }
  .feature-article {
    position: absolute; left: 0; top: 251px; width: 1092px;
    text-align: center; color: var(--nook-red);
    font-size: 40px; line-height: 1;
    letter-spacing: 22px; padding-left: 22px;
  }
  .feature-name {
    position: absolute; left: 0; top: 294px; width: 1092px;
    text-align: center; color: var(--nook-red);
    font-size: 74px; line-height: 1; letter-spacing: -1px;
    white-space: nowrap;
  }
  .feature-rule {
    position: absolute; top: 377px; height: 4px;
    background: var(--nook-red);
  }
  .feature-rule--left { left: 250px; width: 274px; }
  .feature-rule--right { left: 642px; width: 197px; }
  .feature-flourish {
    position: absolute; left: 532px; top: 365px;
    width: 104px; height: 52px;
    border-radius: 26px;
    background: var(--flourish-tint);
  }
  .meadow-band {
    position: absolute; left: 0; bottom: 0;
    width: 1092px; height: 118px;
    background: linear-gradient(180deg, var(--meadow-light) 0%, var(--meadow-deep) 100%);
  }
</style>
</head>
<body>
  <section class="street-sign">
    <div class="partner-name partner-name--nursery">The Harlow Ridge<br>Growers &amp; Nursery</div>

    <div class="brand-divider"></div>

    <div class="partner-name partner-name--commons">Quarry<br>Commons</div>

    <div class="feature-article">THE</div>
    <div class="feature-name">BRAMBLE NOOK</div>

    <div class="feature-rule feature-rule--left"></div>
    <div class="feature-flourish" role="img" aria-label="Decorative red swirl flourish beneath the shop name"></div>
    <div class="feature-rule feature-rule--right"></div>

    <div class="meadow-band" role="img" aria-label="Meadow of green grass with white daisies, yellow flowers and butterflies"></div>
  </section>
</body>
</html>
```